Business Card Design Project

Looking for a business card that our customers will remember. We are a high end Travel Agency.
Need a re-memorable classy business card.
Both sides full color.
Must have the following details.
Voyage Harbor Logo (see attached)
4B Wattle Lane
Penhurst Sydney NSW 2241
Phone: 02 9471 3652
Fax: 02 9563 4417
sales@voyageharbor-example.com.au
Consultant Name
Anything else you think we need

```html
<!DOCTYPE html>
<html lang="en">
<head>
<meta charset="utf-8">
<title>Voyage Harbor Business Card</title>
<link rel="stylesheet" href="https://fonts.googleapis.com/css2?family=Lato:wght@400;700&display=swap">
<style>
  :root {
    --brand-blue: #1f5a8b;
    --brand-blue-light: #2f6fa3;
    --brand-yellow: #f5c21a;
    --ink: #2b2b2b;
    --paper: #ffffff;
    --backdrop: #e9edf0;
  }
  * { box-sizing: border-box; margin: 0; padding: 0; }
  html, body { width: 1200px; height: 960px; overflow: hidden; }
  body {
    background: var(--backdrop);
    font-family: 'Lato', sans-serif;
    color: var(--ink);
    position: relative;
  }
  .card {
    position: absolute;
    left: 280px;
    width: 640px;
    height: 366px;
    overflow: hidden;
    box-shadow: 0 6px 18px rgba(0,0,0,0.15);
  }
  .card--front { top: 80px; background: var(--paper); }
  .card--back { top: 506px; background: var(--brand-blue); }

  .brand-name {
    position: absolute;
    font-weight: 700;
    font-size: 36px;
    letter-spacing: 1px;
  }
  .card--front .brand-name { left: 36px; top: 38px; color: var(--brand-blue); }
  .card--back .brand-name { left: 88px; top: 36px; color: var(--paper); font-size: 30px; }

  .consultant {
    position: absolute;
    left: 40px;
    top: 170px;
    font-size: 16px;
    text-transform: uppercase;
  }
  .consultant__name {
    font-size: 26px;
    font-weight: 700;
    color: var(--brand-blue);
    text-transform: none;
  }
  .consultant__sep { color: var(--ink); margin: 0 4px; }

  .divider {
    position: absolute;
    left: 40px;
    right: 40px;
    top: 210px;
    height: 1.5px;
    background: var(--brand-blue);
  }

  .address {
    position: absolute;
    left: 400px;
    top: 228px;
    font-size: 15px;
    line-height: 22px;
    font-style: normal;
  }

  .contacts {
    position: absolute;
    left: 40px;
    top: 244px;
    list-style: none;
    font-size: 15px;
    line-height: 25px;
  }
  .contacts li { display: flex; align-items: center; gap: 12px; white-space: nowrap; }
  .contacts svg { width: 17px; height: 17px; fill: none; stroke: var(--brand-blue); stroke-width: 1.6; }

  .footer-shape {
    position: absolute;
    inset: 0;
    width: 100%;
    height: 100%;
  }
  .web-address {
    position: absolute;
    right: 20px;
    bottom: 20px;
    color: var(--paper);
    font-size: 14px;
    font-weight: 700;
    white-space: nowrap;
  }

  .back-band {
    position: absolute;
    inset: 0;
    width: 100%;
    height: 100%;
  }
</style>
</head>
<body>

  <section class="card card--front" aria-label="Business card front">
    <svg class="footer-shape" viewBox="0 0 640 366" aria-hidden="true">
      <rect x="0" y="348" width="640" height="18" fill="var(--brand-blue)"/>
      <polygon points="372,302 640,302 640,366 348,366" fill="var(--brand-yellow)"/>
      <polygon points="384,310 640,310 640,366 362,366" fill="var(--brand-blue)"/>
    </svg>

    <div class="brand-name">Voyage Harbor</div>

    <p class="consultant">
      <span class="consultant__name">Mirela Hart</span><span class="consultant__sep">|</span>Consultant
    </p>
    <div class="divider"></div>

    <address class="address">
      4B Wattle Lane<br>
      Penhurst Sydney NSW 2241
    </address>

    <ul class="contacts">
      <li>
        <svg viewBox="0 0 18 18" aria-hidden="true"><rect x="3" y="1.5" width="12" height="15" rx="1.5"/><rect x="5.5" y="4" width="7" height="3"/><path d="M6 10h1M9 10h1M12 10h0.5M6 13h1M9 13h1M12 13h0.5"/></svg>
        02 9471 3652
      </li>
      <li>
        <svg viewBox="0 0 18 18" aria-hidden="true"><rect x="5" y="1.5" width="8" height="5"/><rect x="2" y="6.5" width="14" height="7" rx="1"/><rect x="5" y="11" width="8" height="5.5"/></svg>
        02 9563 4417
      </li>
      <li>
        <svg viewBox="0 0 18 18" aria-hidden="true"><rect x="1.5" y="3.5" width="15" height="11"/><path d="M1.5 3.5l7.5 6 7.5-6"/></svg>
        sales@voyageharbor-example.com.au
      </li>
    </ul>

    <div class="web-address">www.voyageharbor-example.com.au</div>
  </section>

  <section class="card card--back" aria-label="Business card back">
    <svg class="back-band" viewBox="0 0 640 366" preserveAspectRatio="none" aria-hidden="true">
      <path d="M0 150 C 200 135, 420 110, 640 80 L 640 98 C 430 128, 210 158, 0 178 Z" fill="var(--brand-blue-light)" opacity="0.7"/>
    </svg>
    <div class="brand-name">Voyage Harbor</div>
  </section>

</body>
</html>
```